Etiketten für Vodka
Zielgruppe
Herstellung und Abfüllung von Spirituosen
Zielgruppe für die Kubus Range sind Bars, Clubs, Feste/Festivals
Aufgabenstellung
Unsere Kubus-Range umfasst rund 40 Spirituosen und deckt nahezu alles ab, was in einer modernen und gut sortierten Theke nicht fehlen darf.
Zum Jahreswechsel möchten wir die gesamte Range relaunchen und suchen im ersten Schritt ein Vorder-, Rückenetikett und Halsschleife für den Hauptartikel Vodka, welches in nachfolgenden Schritten auf die anderen Artikel übertragen werden soll.
Das Design soll wertig sein, auf unsere eigene Herstellung von Destillaten und Kräuterauszügen hinweisen.
Bei dem bestehenden Design kann der Barkeeper die Sorten leicht unterscheiden, dies soll auch weiterhin so bleiben.
Das Logo 'Kubus' ist eine eingetragen Wort-Bild-Marke und muss im Vorderetikett bestehen bleiben.
Max Größe Vorderetikett: Höhe 150mm, Breite 60mm
Max Größe Rückenetikett: Höhe 100mm, Breite 40mm

```html
<!DOCTYPE html>
<html lang="de">
<head>
<meta charset="utf-8">
<title>Kubus Vodka – Etiketten</title>
<link rel="stylesheet" href="https://fonts.googleapis.com/css2?family=Exo+2:wght@300;400;700&family=Quicksand:wght@500&display=swap">
<style>
  :root {
    --bg: #f3f0ea;
    --navy: #25358f;
    --blue: #2a54a8;
    --steel: #5f7cb8;
    --teal: #1f8aa6;
    --aqua: #34c2c9;
    --sea: #2f9c8c;
    --white: #ffffff;
    --ink: #1a1a1f;
  }
  * { margin: 0; padding: 0; box-sizing: border-box; }
  html, body { width: 1200px; height: 1200px; overflow: hidden; background: var(--bg); }
  body { position: relative; font-family: "Exo 2", sans-serif; color: var(--white); }

  .front-label {
    position: absolute; left: 250px; top: 170px; width: 460px; height: 860px;
    background: linear-gradient(165deg, var(--teal) 0%, var(--navy) 45%, var(--blue) 75%, var(--steel) 100%);
    overflow: hidden; box-shadow: 0 10px 30px rgba(0,0,0,.15);
  }
  .wave-art {
    position: absolute; left: 0; top: 200px; width: 100%; height: 420px;
    background:
      radial-gradient(ellipse 70% 35% at 40% 40%, rgba(47,156,140,.75) 0%, rgba(47,156,140,0) 100%),
      radial-gradient(ellipse 60% 30% at 70% 60%, rgba(52,194,201,.55) 0%, rgba(52,194,201,0) 100%);
  }
  .brand-name {
    position: absolute; top: 170px; left: 0; width: 100%; text-align: center;
    font-weight: 700; font-size: 76px; letter-spacing: 6px; text-transform: uppercase; color: var(--white);
  }
  .product-name {
    position: absolute; top: 430px; left: 0; width: 100%; text-align: center;
    font-weight: 300; font-size: 78px; letter-spacing: 10px; line-height: 1;
  }
  .divider { position: absolute; top: 530px; left: 95px; width: 270px; height: 1px; background: var(--white); }
  .variety {
    position: absolute; top: 548px; left: 0; width: 100%; text-align: center;
    font-weight: 300; font-size: 30px; letter-spacing: 7px;
  }
  .description {
    position: absolute; top: 620px; left: 70px; width: 320px; text-align: center;
    font-family: "Quicksand", sans-serif; font-weight: 500; font-size: 16px; line-height: 1.35;
  }
  .volume {
    position: absolute; top: 760px; left: 0; width: 100%; text-align: center;
    font-family: "Quicksand", sans-serif; font-weight: 500; font-size: 26px;
  }
  .base-band { position: absolute; left: 0; bottom: 0; width: 100%; height: 18px; background: var(--ink); }

  .neck-label {
    position: absolute; left: 790px; top: 170px; width: 170px; height: 480px;
    background: linear-gradient(170deg, var(--teal) 0%, var(--navy) 55%, var(--blue) 100%);
    box-shadow: 0 10px 30px rgba(0,0,0,.15);
  }
  .neck-text {
    position: absolute; left: 50%; top: 50%; transform: translate(-50%, -50%) rotate(-90deg);
    text-align: center; white-space: nowrap;
  }
  .neck-text .product-word { font-weight: 300; font-size: 56px; letter-spacing: 8px; display: block; line-height: 1.1; }
  .neck-text .neck-rule { display: block; height: 1px; background: var(--white); margin: 6px 0 8px; }
  .neck-text .variety-word { font-weight: 300; font-size: 24px; letter-spacing: 6px; display: block; }
</style>
</head>
<body>
  <section class="front-label">
    <div class="wave-art" role="img" aria-label="Abstrakte türkis-grüne Wellenstruktur"></div>
    <div class="brand-name">Kubus</div>
    <div class="product-name">VODKA</div>
    <div class="divider"></div>
    <div class="variety">SORTE</div>
    <p class="description">Lorem ipsum dolor sit amet, consectetuer adipiscing elit, sed diam nonummy nibh euismodamet, consectetuer.</p>
    <div class="volume">750 ml</div>
    <div class="base-band"></div>
  </section>

  <aside class="neck-label">
    <div class="neck-text">
      <span class="product-word">VODKA</span>
      <span class="neck-rule"></span>
      <span class="variety-word">SORTE</span>
    </div>
  </aside>
</body>
</html>
```